Land Buying Company Needs Letterhead for Direct Mail Marketing to Land Owners

We are looking for a professional letterhead that we will be including in our direct mail marketing. We will be sending this to land owners who may be interested in selling or purchasing land.

The letterhead needs to be editable. Headers and footers would look nice, but we are open. We would want it to include our address, website, phone, and email info. For right now the address to use for design purposes would the following:

Address: 415 Bramwell Avenue #600
Dallas, TX 75219
Website - www.quillridgeacres.example
Email - info@quillridgeacres.example
Phone - 866-402-ACRE

I have attached our logo zip file that we just had done on Pixel Guild. Let me know what questions you have, and thank you.

```html
<!DOCTYPE html>
<html lang="en">
<head>
<meta charset="utf-8">
<title>Quill Ridge Acres Letterhead</title>
<link rel="stylesheet" href="https://fonts.googleapis.com/css2?family=Montserrat:wght@600;700&family=Open+Sans:wght@400;600&family=Poppins:wght@400;500&display=swap">
<style>
  :root {
    --bg: #ececea;
    --paper: #ffffff;
    --lime: #8dc63f;
    --forest: #46612c;
    --ink: #1c1c1c;
    --black: #0b0b0b;
    --white: #ffffff;
  }
  * { margin: 0; padding: 0; box-sizing: border-box; }
  html, body { width: 1200px; height: 864px; overflow: hidden; background: var(--bg); }
  .canvas { position: relative; width: 1200px; height: 864px; }
  .letterhead {
    position: absolute; left: 310px; top: 22px; width: 580px; height: 820px;
    background: var(--paper); overflow: hidden;
    box-shadow: 0 6px 18px rgba(0,0,0,0.12);
    font-family: "Open Sans", Arial, sans-serif; color: var(--ink);
  }
  .top-band { position: absolute; left: 0; top: 0; width: 100%; height: 20px; background: var(--lime); }
  .brand-banner { position: absolute; left: 168px; top: 0; width: 250px; height: 112px; }
  .brand {
    position: absolute; left: 168px; top: 28px; width: 250px;
    display: flex; align-items: center; justify-content: center; gap: 10px;
  }
  .brand-dot { width: 30px; height: 30px; border-radius: 50%; background: var(--white); flex: none; }
  .brand-name {
    font-family: "Montserrat", Arial, sans-serif; font-weight: 700; font-size: 15px;
    letter-spacing: 1px; color: var(--lime); line-height: 1.1;
  }
  .recipient { position: absolute; left: 78px; top: 180px; font-size: 9px; line-height: 11.5px; }
  .recipient .name { font-family: "Montserrat", Arial, sans-serif; font-weight: 700; font-size: 9.5px; }
  .letter-body { position: absolute; left: 78px; top: 262px; width: 440px; font-size: 8.8px; line-height: 11.5px; }
  .letter-body p { margin-bottom: 11.5px; }
  .signature { position: absolute; left: 78px; top: 512px; width: 130px; height: 28px; background: linear-gradient(90deg, rgba(70,97,44,0.18), rgba(70,97,44,0.05)); border-radius: 3px; }
  .signer { position: absolute; left: 78px; top: 546px; font-size: 9px; line-height: 11.5px; }
  .signer .name { font-weight: 600; font-size: 9.5px; }
  .footer { position: absolute; left: 0; bottom: 0; width: 100%; height: 86px; }
  .footer-band { position: absolute; left: 0; bottom: 6px; width: 100%; height: 56px; background: var(--black); border-top: 3px solid var(--lime); }
  .footer-base { position: absolute; left: 0; bottom: 0; width: 100%; height: 6px; background: var(--lime); }
  .contact {
    position: absolute; top: 0; width: 145px; text-align: center;
    font-family: "Poppins", Arial, sans-serif; font-size: 6.6px; line-height: 9px; color: var(--white);
  }
  .contact svg { display: block; margin: 0 auto 12px; }
  .contact-address { left: 0; }
  .contact-web { left: 145px; }
  .contact-mail { left: 290px; }
  .contact-phone { left: 435px; }
</style>
</head>
<body>
<div class="canvas">
  <article class="letterhead">
    <div class="top-band"></div>
    <svg class="brand-banner" viewBox="0 0 250 112" aria-hidden="true">
      <polygon points="0,0 250,0 250,82 125,112 0,82" fill="var(--forest)"/>
    </svg>
    <div class="brand">
      <span class="brand-dot"></span>
      <span class="brand-name">QUILL RIDGE ACRES</span>
    </div>

    <div class="recipient">
      <div class="name">Dear Devan</div>
      <div>Senior Executive</div>
      <div>Address goes here. Street, City, Country</div>
      <div>contact@yourmail.com</div>
      <div>000-987-654-321</div>
    </div>

    <div class="letter-body">
      <p>Dear Recipient,</p>
      <p>Write the body of your letter here. To update any of the information in this letter, simply click and start typing!</p>
      <p>Want to customize your color palette? Just go to the Design ribbon, and select Colors from the list. If you choose a color palette that you like, the colors of the header images will update, as will the text colors. Make the document yours!</p>
      <p>Want to change the fonts that are used? That is just as easy to update. Just go to the Design ribbon and choose Fonts from the menu options. You can use a built-in font combination or choose one of your own.</p>
      <p>Lorem ipsum dolor sit amet, consectetur adipisicing elit, sed do eiusmod tempor incididunt ut labore et dolore magna aliqua. Ut enim ad minim veniam, quis nostrud exercitation ullamco laboris nisi ut aliquip ex ea commodo consequat. Duis aute irure dolor in reprehenderit in voluptate velit esse cillum dolore eu fugiat nulla pariatur. Excepteur sint occaecat cupidatat non proident, sunt in culpa qui officia deserunt mollit anim id est laborum.</p>
      <p>Sed ut perspiciatis unde omnis iste natus error sit voluptatem accusantium doloremque laudantium, totam rem aperiam, eaque ipsa quae ab illo inventore veritatis et quasi architecto beatae vitae dicta sunt explicabo. Nemo enim ipsam voluptatem quia voluptas sit aspernatur aut odit veritatis et quasi architecto aut.</p>
    </div>

    <div class="signature" role="img" aria-label="Handwritten signature of Marcus Ellery"></div>
    <div class="signer">
      <div class="name">Marcus Ellery</div>
      <div>General Manager</div>
    </div>

    <footer class="footer">
      <div class="footer-band"></div>
      <div class="footer-base"></div>
      <div class="contact contact-address">
        <svg width="22" height="24" viewBox="0 0 22 24" aria-hidden="true">
          <polygon points="0,0 22,0 22,18 11,24 0,18" fill="var(--forest)"/>
          <path d="M11 5a4 4 0 0 0-4 4c0 3 4 7 4 7s4-4 4-7a4 4 0 0 0-4-4z" fill="var(--white)"/>
          <circle cx="11" cy="9" r="1.5" fill="var(--forest)"/>
        </svg>
        Address: 415 Bramwell Avenue #600<br>Dallas, TX 75219
      </div>
      <div class="contact contact-web">
        <svg width="22" height="24" viewBox="0 0 22 24" aria-hidden="true">
          <polygon points="0,0 22,0 22,18 11,24 0,18" fill="var(--forest)"/>
          <g fill="none" stroke="var(--white)" stroke-width="1">
            <circle cx="11" cy="10" r="5"/>
            <ellipse cx="11" cy="10" rx="2.2" ry="5"/>
            <line x1="6" y1="10" x2="16" y2="10"/>
          </g>
        </svg>
        www.quillridgeacres.example
      </div>
      <div class="contact contact-mail">
        <svg width="22" height="24" viewBox="0 0 22 24" aria-hidden="true">
          <polygon points="0,0 22,0 22,18 11,24 0,18" fill="var(--forest)"/>
          <rect x="5" y="6" width="12" height="8" fill="var(--white)"/>
          <polyline points="5,6 11,11 17,6" fill="none" stroke="var(--forest)" stroke-width="1"/>
        </svg>
        info@quillridgeacres.example
      </div>
      <div class="contact contact-phone">
        <svg width="22" height="24" viewBox="0 0 22 24" aria-hidden="true">
          <polygon points="0,0 22,0 22,18 11,24 0,18" fill="var(--forest)"/>
          <path d="M7.5 5.5l2 0 1 3-1.3 1a6 6 0 0 0 2.8 2.8l1-1.3 3 1v2c0 .6-.5 1-1 1A9 9 0 0 1 6.5 6.5c0-.6.4-1 1-1z" fill="var(--white)"/>
        </svg>
        866-402-ACRE
      </div>
    </footer>
  </article>
</div>
</body>
</html>
```